InfoGraphic for Security Pyramid

I've created an infographic that I would like to be redone more professionally. you can see the page in this powerpoint called the pyramid of security. What I'd like done is to replace the background graphic with a new icon in a cartoony format like the one behind end point protection as an example (thats a stock photo).

Target Market(s)

Business Owners

Font styles to use
Sans Serif

Colors
ec1f27
0355a3
f37122

Requirements
Must have
• Consistent images, text must be editable.

```html
<!DOCTYPE html>
<html lang="en">
<head>
<meta charset="utf-8">
<title>Security Pyramid</title>
<link rel="stylesheet" href="https://fonts.googleapis.com/css2?family=Arimo:wght@400&display=swap">
<style>
  :root {
    --navy: #0b0b5f;
    --red: #f5163f;
    --tier-light: #f8f8f8;
    --tier-grey: #e6e6e6;
    --white: #ffffff;
    --icon-on-light: #c9c5dc;
    --icon-on-dark: #3a3a86;
  }
  html, body {
    margin: 0;
    padding: 0;
    width: 1200px;
    height: 796px;
    overflow: hidden;
    background: var(--white);
  }
  .security-pyramid {
    display: block;
    width: 1200px;
    height: 796px;
  }
  .tier-label {
    font-family: "Arimo", Arial, sans-serif;
    font-size: 17px;
    text-anchor: middle;
  }
  .tier-label--dark { fill: var(--navy); }
  .tier-label--light { fill: var(--white); }
  .fill-navy { fill: var(--navy); }
  .fill-white { fill: var(--white); }
  .fill-light { fill: var(--tier-light); }
  .fill-grey { fill: var(--tier-grey); }
  .icon-slot--on-light { fill: url(#slot-light); }
  .icon-slot--on-dark { fill: url(#slot-dark); }
</style>
</head>
<body>
<svg class="security-pyramid" viewBox="0 0 1000 663.3" role="img" aria-label="Pyramid of security layers">
  <defs>
    <linearGradient id="slot-light" x1="0" y1="0" x2="1" y2="1">
      <stop offset="0" stop-color="#f7c9d3"/>
      <stop offset="1" stop-color="#c9c5dc"/>
    </linearGradient>
    <linearGradient id="slot-dark" x1="0" y1="0" x2="1" y2="1">
      <stop offset="0" stop-color="#5a2a78"/>
      <stop offset="1" stop-color="#2a2a7a"/>
    </linearGradient>
  </defs>

  <g class="tiers">
    <polygon class="tier tier--training fill-light" points="500,85 406,224 594,224"/>
    <polygon class="tier tier--filtering fill-grey" points="406,224 500,224 500,367 310,367"/>
    <polygon class="tier tier--scanning fill-navy" points="500,224 594,224 690,367 500,367"/>
    <polygon class="tier tier--intel fill-navy" points="310,367 404,367 404,510 213,510"/>
    <polygon class="tier tier--assets fill-white" points="404,367 596,367 596,510 404,510"/>
    <polygon class="tier tier--admin fill-grey" points="596,367 690,367 787,510 596,510"/>
  </g>

  <rect class="icon-slot icon-slot--on-light" x="457" y="137" width="86" height="55" rx="8"
        role="img" aria-label="Icon: person lifting a barbell, representing user training"/>
  <text class="tier-label tier-label--dark" x="500" y="214">User Training</text>

  <rect class="icon-slot icon-slot--on-light" x="392" y="272" width="72" height="56" rx="8"
        role="img" aria-label="Icon: magnifying glass, representing web filtering"/>
  <text class="tier-label tier-label--dark" x="425" y="353">Web Filtering</text>

  <rect class="icon-slot icon-slot--on-dark" x="541" y="258" width="94" height="80" rx="8"
        role="img" aria-label="Icon: target with crosshair over a scan line, representing continuous scanning"/>
  <text class="tier-label tier-label--light" x="593" y="357">Continous Scanning</text>

  <rect class="icon-slot icon-slot--on-dark" x="286" y="416" width="88" height="48" rx="8"
        role="img" aria-label="Icon: open eye, representing threat intelligence"/>
  <text class="tier-label tier-label--light" x="330" y="498">Threat Intel</text>

  <rect class="icon-slot icon-slot--on-light" x="466" y="402" width="80" height="66" rx="8"
        role="img" aria-label="Icon: office building with a check mark, representing asset management"/>
  <text class="tier-label tier-label--dark" x="500" y="498">Asset Menagement</text>

  <rect class="icon-slot icon-slot--on-light" x="638" y="410" width="98" height="52" rx="8"
        role="img" aria-label="Icon: three figures of decreasing size, representing minimized admin rights"/>
  <text class="tier-label tier-label--dark" x="690" y="498">Minimize Admin</text>
</svg>
</body>
</html>
```